One of a Kind Clean Business Card

We need to design a new business card template for our company. Our company designs and produced merchandising displays. You can see a sample of what we produce on our site www.qorvatfixtures.com. I have uploaded our logo in vector format, as well as a picture of our current business cards. We want a totally different look. We want simple and clean, looking forward to seeing what people create.
Updates

I would like to update the address for Tellur Display Group Inc. 418 N Brindle Ave Arlington Heights, IL 60817 Would also note. No QR codes

Industry/Entity Type

Business

Contact Information for Business Card

Need a 1 sided business card designed.

Font styles to use
Serif

Requirements
Must have
• Easy to view; Clean Design
Nice to have
• Features that promote engineering and creativity
Should not have
• Too much clutter, keep it simple

```html
<!DOCTYPE html>
<html lang="en">
<head>
<meta charset="utf-8">
<title>Tellur Display Group Inc. — Business Card</title>
<link rel="stylesheet" href="https://fonts.googleapis.com/css2?family=Questrial&family=Oswald:wght@500&display=swap">
<style>
  :root {
    --backdrop: #d9d6d1;
    --card: #0b0b0c;
    --card-sheen: #1c1c1e;
    --ink: #f2f2f2;
    --accent: #b3232f;
  }
  * { margin: 0; padding: 0; box-sizing: border-box; }
  html, body {
    width: 1200px; height: 1022px; overflow: hidden;
    background: var(--backdrop);
  }
  .canvas {
    width: 1200px; height: 1022px;
    display: flex; align-items: center; justify-content: center;
  }
  .card {
    position: relative;
    width: 1000px; height: 571px;
    background: linear-gradient(135deg, var(--card-sheen) 0%, var(--card) 55%);
    color: var(--ink);
    font-family: "Questrial", "Helvetica Neue", Arial, sans-serif;
    box-shadow: 0 20px 50px rgba(0,0,0,.25);
  }
  .card__lines { position: absolute; inset: 0; }
  .brand {
    position: absolute; left: 60px; top: 190px;
    display: flex; align-items: center; gap: 16px;
    font-size: 40px; letter-spacing: .5px; color: var(--ink);
  }
  .brand__mark {
    width: 18px; height: 18px; border: 2px solid var(--ink);
  }
  .holder {
    position: absolute; right: 60px; top: 238px;
    font-family: "Oswald", "Arial Narrow", sans-serif;
    font-weight: 500; font-size: 34px; color: var(--accent);
  }
  .address {
    position: absolute; right: 60px; top: 338px;
    text-align: right; font-size: 24px; line-height: 1.5;
  }
  .contacts {
    position: absolute; left: 330px; top: 340px;
    list-style: none; font-size: 24px; line-height: 1.6;
  }
  .contacts li { display: flex; align-items: center; gap: 16px; }
  .contacts svg { width: 20px; height: 20px; fill: none; stroke: var(--accent); stroke-width: 2; }
</style>
</head>
<body>
<main class="canvas">
  <section class="card" aria-label="Business card">
    <svg class="card__lines" viewBox="0 0 1000 571" aria-hidden="true">
      <path d="M0 300 H940" stroke="var(--accent)" stroke-width="3" fill="none"/>
      <path d="M300 300 V520" stroke="var(--accent)" stroke-width="3" fill="none"/>
    </svg>

    <div class="brand">
      <span class="brand__mark" aria-hidden="true"></span>
      <span class="brand__name">Tellur Display Group Inc.</span>
    </div>

    <h1 class="holder">Rob Vantreck</h1>

    <address class="address">
      418 N Brindle Ave<br>
      Arlington Heights, IL 60817
    </address>

    <ul class="contacts">
      <li>
        <svg viewBox="0 0 20 20" aria-hidden="true"><path d="M4 2 L8 2 L9 6 L7 8 Q9 12 12 13 L14 11 L18 12 L18 16 Q10 18 4 10 Q2 6 4 2 Z"/></svg>
        815-555-0142
      </li>
      <li>
        <svg viewBox="0 0 20 20" aria-hidden="true"><rect x="5" y="2" width="10" height="16" rx="1.5"/><path d="M9 15 H11"/></svg>
        312-555-0178
      </li>
      <li>
        <svg viewBox="0 0 20 20" aria-hidden="true"><rect x="2" y="4" width="16" height="12"/><path d="M2 4 L10 11 L18 4"/></svg>
        rvantreck@qorvatfixtures.com
      </li>
      <li>
        <svg viewBox="0 0 20 20" aria-hidden="true"><circle cx="10" cy="10" r="8"/><path d="M2 10 H18 M10 2 Q5 10 10 18 M10 2 Q15 10 10 18"/></svg>
        www.qorvatfixtures.com
      </li>
    </ul>
  </section>
</main>
</body>
</html>
```